Harbor Relay Group Letterhead Design

The project name sums it up. Just need a professional letterhead design / template we can use in our marketing folders.

Here's the address / contact info for the letterhead: Harbor Relay Group 4815 Maple Crest Ave Suite 210 League City, Texas 77419 346-507-3846 www.harborrelaygroup.us support@harborrelaygroup.us

```html
<!DOCTYPE html>
<html lang="en">
<head>
<meta charset="utf-8">
<title>Harbor Relay Group Letterhead</title>
<link rel="stylesheet" href="https://fonts.googleapis.com/css2?family=Arimo:wght@400;700&family=Source+Sans+3:wght@400;600;700&display=swap">
<style>
  :root {
    --backdrop: #d9d9d9;
    --paper: #ffffff;
    --ink: #1a1a1a;
    --body-ink: #2b2b2b;
    --brand-blue: #0a3fb8;
    --band-blue: #1046c4;
    --band-blue-deep: #0a35a3;
    --band-black: #0b0b0b;
  }
  * { box-sizing: border-box; margin: 0; padding: 0; }
  html, body {
    width: 1200px;
    height: 880px;
    overflow: hidden;
    background: var(--backdrop);
  }
  .letterhead {
    position: absolute;
    left: 295px;
    top: 20px;
    width: 610px;
    height: 840px;
    background: var(--paper);
    box-shadow: 0 2px 10px rgba(0,0,0,0.12);
    overflow: hidden;
  }
  .brand {
    position: absolute;
    left: 50px;
    top: 66px;
    display: flex;
    align-items: center;
    gap: 9px;
  }
  .brand-mark {
    width: 26px;
    height: 26px;
    background: var(--brand-blue);
  }
  .brand-name {
    font-family: "Arimo", Arial, sans-serif;
    font-weight: 700;
    font-size: 17px;
    color: var(--brand-blue);
    letter-spacing: 0.2px;
  }
  .header-address {
    position: absolute;
    left: 333px;
    top: 81px;
    width: 245px;
    font-family: "Arimo", Arial, sans-serif;
    font-size: 9.6px;
    line-height: 12px;
    color: var(--ink);
  }
  .letter-body {
    position: absolute;
    left: 93px;
    top: 262px;
    width: 450px;
    font-family: "Source Sans 3", "Myriad Pro", sans-serif;
    font-size: 11.2px;
    line-height: 14.5px;
    color: var(--body-ink);
    font-weight: 600;
  }
  .letter-subject {
    font-weight: 700;
    margin-bottom: 14px;
  }
  .letter-body p { margin-bottom: 14px; }
  .letter-signoff { margin-top: 42px; }
  .footer-contact {
    position: absolute;
    left: 0;
    right: 0;
    top: 741px;
    display: flex;
    justify-content: center;
    align-items: center;
    font-family: "Arimo", Arial, sans-serif;
    font-size: 10.6px;
    color: var(--ink);
  }
  .footer-item { padding: 0 11px; }
  .footer-divider {
    width: 1.5px;
    height: 18px;
    background: var(--brand-blue);
  }
  .band-black {
    position: absolute;
    left: 0; right: 0;
    top: 782px;
    height: 11px;
    background: var(--band-black);
  }
  .band-blue {
    position: absolute;
    left: 0; right: 0;
    top: 806px;
    height: 34px;
    background: linear-gradient(100deg, var(--band-blue-deep), var(--band-blue) 45%, var(--band-blue-deep));
  }
</style>
</head>
<body>
  <main class="letterhead">
    <div class="brand">
      <span class="brand-mark"></span>
      <span class="brand-name">Harbor Relay Group</span>
    </div>

    <div class="header-address">Harbor Relay Group 4815 Maple Crest Ave Suite 210 League City</div>

    <section class="letter-body">
      <div class="letter-subject">Duis aute irure dolor</div>
      <p>Lorem ipsum dolor sit amet, consectetur adipiscing elit, sed do eiusmod tempor incididunt ut labore et dolore magna aliqua. Ut enim ad minim veniam, quis nostrud exercitation ullamco laboris nisi ut aliquip ex ea commodo consequat.</p>
      <p>Duis aute irure dolor in reprehenderit in voluptate velit esse cillum dolore eu fugiat nulla pariatur. Excepteur sint occaecat cupidatat non proident, sunt in culpa qui officia deserunt mollit anim id est laborum. Lorem ipsum dolor sit amet, consectetur adipiscing elit, sed do eiusmod tempor incididunt ut labore et dolore magna aliqua. Ut enim ad minim veniam, quis nostrud exercitation ullamco laboris nisi ut aliquip ex ea commodo consequat. Duis aute irure dolor in reprehenderit in voluptate velit esse cillum dolore eu fugiat nulla pariatur. Excepteur sint occaecat cupidatat non proident, sunt in culpa qui officia deserunt mollit anim id est laborum.</p>
      <p>Lorem ipsum dolor sit amet, consectetur adipiscing elit, sed do eiusmod tempor incididunt ut labore et dolore magna aliqua. Ut enim ad minim veniam, quis nostrud exercitation.</p>
      <div class="letter-signoff">Lorem ipsum,<br>M dolor sit amet</div>
    </section>

    <footer class="footer-contact">
      <span class="footer-item">Texas 77419 346-507-3846</span>
      <span class="footer-divider"></span>
      <span class="footer-item">www.harborrelaygroup.us</span>
      <span class="footer-divider"></span>
      <span class="footer-item">support@harborrelaygroup.us</span>
    </footer>

    <div class="band-black"></div>
    <div class="band-blue" role="img" aria-label="Blue footer band with a faint abstract line texture"></div>
  </main>
</body>
</html>
```